2013 Global Campus Assembly

The Global Campus Assembly is searching for a poster design that can also serve as cover art for its conference program (8.5x11). The event is entering its sixth year and will be held in Vancouver, Canada. It is modeled after the Planetary Trade Council, and meets yearly to discuss the University, how it is formed, and its place in an ever changing society.

Many perspectives are shared as the conference attracts people from all over the world. This past year's meeting had almost 30 countries represented.

Issues and discussions include loss of funding, especially in times of economic turmoil, the necessity of college degrees, electronic education, the place of the University in the world, etc.

The theme for 2013 will revolve around Higher Education and the Future of Democracy.

We would like something bold and indicative of the ideas to be discussed, but not controversial. No current color preferences. Ideas that pertain to democracy and/or Vancouver are welcome.

Target Market(s)

Scholars, Teachers, Administrators, Students, Provosts, Deans, Distance Educators

Industry/Entity Type

Electronic

Requirements
Must have
• Please include text:
Sixth Global Campus Assembly
10-11 January 2013
NPL-Harwick Plaza
Vancouver, Canada

```html
<!DOCTYPE html>
<html lang="en">
<head>
<meta charset="utf-8">
<title>Sixth Global Campus Assembly</title>
<link rel="stylesheet" href="https://fonts.googleapis.com/css2?family=PT+Sans+Narrow:wght@400&display=swap">
<style>
  :root {
    --sky: #00ffff;
    --ink: #000000;
    --paper: #ffffff;
  }
  html, body {
    margin: 0;
    padding: 0;
    overflow: hidden;
    background: var(--sky);
  }
  .poster {
    display: block;
    width: 927px;
    height: 1200px;
    background: var(--sky);
  }
  .theme-word,
  .event-details,
  .event-title {
    font-family: "PT Sans Narrow", "Arial Narrow", sans-serif;
    font-weight: 400;
    fill: var(--ink);
  }
  .theme-word { font-size: 76px; }
  .theme-word--slanted { font-style: italic; }
  .event-details { font-size: 40px; }
  .event-title { font-size: 92px; }
</style>
</head>
<body>
<svg class="poster" width="927" height="1200" viewBox="0 0 927 1200" xmlns="http://www.w3.org/2000/svg">
  <defs>
    <radialGradient id="megaphone-tone" cx="0.55" cy="0.45" r="0.6">
      <stop offset="0" stop-color="#ffffff"/>
      <stop offset="0.45" stop-color="#8a8a8a"/>
      <stop offset="1" stop-color="#000000"/>
    </radialGradient>
  </defs>

  <rect class="megaphone-area" x="113" y="316" width="395" height="376" rx="40"
        fill="url(#megaphone-tone)" role="img"
        aria-label="Black and white megaphone pointing right toward the theme words"/>

  <g class="theme-words">
    <text class="theme-word" transform="translate(546 256) rotate(-15)" textLength="168" lengthAdjust="spacingAndGlyphs">People</text>
    <text class="theme-word" transform="translate(571 330) rotate(-10)" textLength="268" lengthAdjust="spacingAndGlyphs">Democracy</text>
    <text class="theme-word" transform="translate(587 411) rotate(-4)" textLength="222" lengthAdjust="spacingAndGlyphs">Economy</text>
    <text class="theme-word" transform="translate(595 496)" textLength="176" lengthAdjust="spacingAndGlyphs">Debate</text>
    <text class="theme-word" transform="translate(591 600) rotate(2)" textLength="244" lengthAdjust="spacingAndGlyphs">Education</text>
    <text class="theme-word theme-word--slanted" transform="translate(584 700) rotate(6)" textLength="144" lengthAdjust="spacingAndGlyphs">World</text>
  </g>

  <g class="event-info">
    <text class="event-details" x="893" y="985" text-anchor="end">10-11 January 2013</text>
    <text class="event-details" x="893" y="1037" text-anchor="end">NPL-Harwick Plaza. Vancouver, Canada</text>
    <text class="event-title" x="31" y="1140" textLength="857" lengthAdjust="spacingAndGlyphs">Sixth Global Campus Assembly</text>
  </g>
</svg>
</body>
</html>
```